Redesign PixelHarbor's Designer Account Home Page

Are a web designer? New to PixelHarbor? This contest is for you!

We want you to redesign PixelHarbor's designer account home page. We're looking for bold and innovative ideas to make this page a useful and fun experience for you and your fellow designers.

Only new registrants this month are eligible to enter this contest and win prizes.

Your task:
* We want you to put your web design skills to the test and re-design the My Account home page ("Overview") on PixelHarbor to make it more functional and engaging for designers on PixelHarbor.
* The page you are redesigning is here: http://www.pixelharbor-example.com/my-profile.
* Your design should allow for the same functionality as the existing page, though you don't need to replicate the same elements (buttons) or the same menu structure.
* Your design must fit with the branding of the site.
* You must provide a brief outline of what changes you made and why when you upload your design
* 1 submission per designer - make it your best work!
* Pls see "Must haves" for requirements.

Deadline:
* Submit before 12:00am 1st September UTC. Pls convert this deadline to your local timezone and take note of the local time and date

Prizes: $1,000 to win
* First prize for the best design is $700
* Second prize is $200
* Third prize is $100

If you started from scratch, how would you design the MyAccount page on PixelHarbor?

Good luck & have fun!

Mel / The PixelHarbor Team

Target Market(s)

PixelHarbor designers

Number of Pages Required

1 page

Requirements
Must have
• Dimensions: 1200 x 1000 px
• Minimum 150-300 dpi
• Your design must adhere to our quality standards to be eligible to receive a prize
• Submissions must be created in Adobe Creative Suite (Illustrator or Photoshop)
• Your design must fit with the branding of the PixelHarbor site.
• Only new registrants this month are eligible to enter and win prizes.

```html
<!DOCTYPE html>
<html lang="en">
<head>
<meta charset="utf-8">
<title>PixelHarbor – My Account Overview</title>
<link rel="stylesheet" href="https://fonts.googleapis.com/css2?family=Open+Sans:wght@400;600;700&display=swap">
<style>
:root{
  --topbar:#2a2d31;
  --crumb:#eef0f2;
  --blue:#1e8ed6;
  --blue-dark:#1677bb;
  --link:#1e8ed6;
  --green:#7cc043;
  --page:#e9ecef;
  --card:#ffffff;
  --line:#dde1e5;
  --text:#4a4f55;
  --muted:#8a9098;
  --white:#ffffff;
}
*{box-sizing:border-box;margin:0;padding:0}
html,body{width:893px;height:1200px;overflow:hidden}
body{font-family:"Open Sans",Arial,sans-serif;background:var(--page);color:var(--text);font-size:9px;line-height:1.45}
.topbar{height:26px;background:var(--topbar);display:flex;align-items:center;padding:0 39px;color:#c8ccd0}
.brand{display:flex;align-items:center;gap:5px;color:var(--white);font-weight:700;font-size:12px;margin-right:18px}
.brand-dot{width:10px;height:10px;border-radius:50%;background:var(--blue)}
.topnav{display:flex;gap:12px;font-size:8px}
.topbar-right{margin-left:auto;display:flex;align-items:center;gap:8px;font-size:8px}
.profile-menu{background:#3c4046;padding:3px 8px;border-radius:2px;color:var(--white)}
.post-btn{background:var(--green);color:var(--white);padding:3px 10px;border-radius:2px;font-weight:600}
.crumbs{height:16px;background:var(--crumb);display:flex;align-items:center;gap:8px;padding:0 39px;font-size:7.5px;color:var(--muted);border-bottom:1px solid var(--line)}
.crumbs svg{width:8px;height:8px}
.hero{height:266px;background:linear-gradient(90deg,var(--blue-dark),var(--blue) 55%,#2aa0e6);position:relative;padding:18px 39px 0;color:var(--white)}
.avatar{position:absolute;left:39px;top:18px;width:126px;height:162px;background:var(--white);padding:5px}
.avatar-photo{width:100%;height:100%;background:linear-gradient(160deg,#c9d3dc,#7f8c99)}
.votes{position:absolute;left:56px;top:196px;display:flex;gap:20px;align-items:center;font-size:10px;font-weight:600}
.votes span{display:flex;align-items:center;gap:5px}
.votes svg{width:16px;height:16px;fill:var(--white)}
.hero-info{position:absolute;left:192px;top:24px;width:390px}
.hero-name{font-size:22px;font-weight:600;line-height:1.2}
.hero-earnings{font-size:12px;margin:4px 0 8px}
.hero-bio{font-size:8.5px;line-height:1.6;opacity:.95}
.hero-actions{display:flex;gap:24px;margin-top:14px}
.btn{font-size:8.5px;font-weight:600;padding:6px 14px;border-radius:2px}
.btn-light{background:var(--white);color:var(--text)}
.btn-green{background:var(--green);color:var(--white)}
.tabs{height:52px;background:var(--card);display:flex;align-items:stretch;padding:0 39px;gap:0;border-bottom:1px solid var(--line)}
.tab{flex:1;display:flex;align-items:center;justify-content:center;gap:6px;font-size:10px;color:var(--text);border-bottom:3px solid transparent}
.tab svg{width:12px;height:12px;stroke:var(--muted);fill:none;stroke-width:1.6}
.tab.active{border-bottom-color:var(--blue);color:var(--blue)}
.tab.active svg{stroke:var(--blue)}
.content{padding:0 39px}
.section-head{display:flex;justify-content:space-between;align-items:baseline;margin:18px 0 8px}
.section-title{font-size:15px;font-weight:600;color:var(--link)}
.see-all{font-size:8px;color:var(--muted)}
.card{background:var(--card);border:1px solid var(--line)}
.job{position:relative;padding:14px 16px 12px 36px;height:91px;border-bottom:1px solid var(--line)}
.job:last-child{border-bottom:0}
.job-row{display:flex;align-items:center}
.job-title{font-size:11.5px;color:var(--link);font-weight:600;flex:1}
.job-meta{display:flex;gap:18px;font-size:8.5px;color:var(--muted);align-items:center}
.job-meta span{display:flex;align-items:center;gap:4px}
.job-meta svg{width:9px;height:9px;stroke:var(--muted);fill:none;stroke-width:1.5}
.job-desc{margin-top:10px;font-size:8px;color:var(--muted);width:540px;line-height:1.6}
.watch-tag{position:absolute;left:-6px;top:14px;width:56px;height:62px;background:var(--blue);color:var(--white);font-size:7px;text-align:center;padding-top:30px;line-height:1.2}
.watch-tag::before{content:"";position:absolute;left:22px;top:12px;width:12px;height:12px;border-radius:50%;border:1.5px solid var(--white)}
.job.featured{padding-left:66px}
.badges{height:84px;display:flex;align-items:center;justify-content:space-around;padding:0 18px}
.badge{width:52px;height:52px;border-radius:50%;background:var(--blue);border:4px solid #cfe6f6;display:flex;align-items:center;justify-content:center}
.badge i{width:18px;height:18px;background:var(--white);border-radius:3px;opacity:.9}
.badge:nth-child(even) i{border-radius:50%}
.review{padding:14px 16px 12px;border-bottom:1px solid var(--line)}
.review-head{display:flex;align-items:center;gap:10px}
.review-title{font-size:11.5px;color:var(--link);font-weight:600}
.stars{display:flex;gap:1px}
.stars svg{width:9px;height:9px;fill:#f2b21b}
.review-date{margin-left:auto;font-size:8px;color:var(--muted)}
.review-text{margin-top:8px;font-size:8px;color:var(--muted);line-height:1.6;width:620px}
</style>
</head>
<body>
<header class="topbar">
  <div class="brand"><span class="brand-dot"></span>PixelHarbor</div>
  <nav class="topnav"><span>Find Designers</span><span>Browse Contests</span><span>How it Works</span><span>Community</span><span>Support</span></nav>
  <div class="topbar-right"><span class="profile-menu">My Profile ▾</span><span class="post-btn">Post Project</span></div>
</header>
<div class="crumbs">
  <svg viewBox="0 0 10 10"><path d="M1 5 5 1l4 4H8v4H6V6H4v3H2V5z" fill="#8a9098"/></svg>
  <span>Home</span><span>›</span><span>My Profile</span>
</div>

<section class="hero">
  <div class="avatar"><div class="avatar-photo" role="img" aria-label="Portrait photo of the designer"></div></div>
  <div class="votes">
    <span><svg viewBox="0 0 16 16"><path d="M2 7h3v8H2zM6 15h6.5a1.5 1.5 0 0 0 1.4-1l1.6-5A1.5 1.5 0 0 0 14 7H10l.6-3.5A1.5 1.5 0 0 0 8 2.5L6 7z"/></svg>12</span>
    <span><svg viewBox="0 0 16 16"><path d="M2 1h3v8H2zM6 1h6.5a1.5 1.5 0 0 1 1.4 1l1.6 5A1.5 1.5 0 0 1 14 9H10l.6 3.5A1.5 1.5 0 0 1 8 13.5L6 9z"/></svg>2</span>
  </div>
  <div class="hero-info">
    <h1 class="hero-name">Reid M. Castell</h1>
    <p class="hero-earnings">Earnings: $30,456</p>
    <p class="hero-bio">Brand and web designer with ten years of experience crafting logos, landing pages and print pieces for small businesses. I love clean layouts, bold color and clear type. Available for new projects, long term partnerships and quick turnaround jobs. Reach out anytime to discuss your ideas.</p>
    <div class="hero-actions"><span class="btn btn-light">Update a Portfolio</span><span class="btn btn-green">Edit a design brief now</span></div>
  </div>
</section>

<nav class="tabs">
  <div class="tab active"><svg viewBox="0 0 12 12"><circle cx="6" cy="6" r="4.5"/></svg>Overview</div>
  <div class="tab"><svg viewBox="0 0 12 12"><rect x="1.5" y="3" width="9" height="6.5"/><path d="M1.5 3 6 7l4.5-4"/></svg>Invites</div>
  <div class="tab"><svg viewBox="0 0 12 12"><path d="M6 9V2M3 5l3-3 3 3M2 10.5h8"/></svg>Submissions</div>
  <div class="tab"><svg viewBox="0 0 12 12"><path d="M1 6s2-3.5 5-3.5S11 6 11 6 9 9.5 6 9.5 1 6 1 6z"/><circle cx="6" cy="6" r="1.5"/></svg>Watchlist</div>
  <div class="tab"><svg viewBox="0 0 12 12"><circle cx="6" cy="4" r="2.3"/><path d="M1.8 11c.5-2.5 2.2-3.6 4.2-3.6s3.7 1.1 4.2 3.6"/></svg>My Profile</div>
</nav>

<main class="content">
  <div class="section-head"><h2 class="section-title">Recommended Jobs</h2><span class="see-all">See all</span></div>
  <div class="card">
    <article class="job">
      <div class="job-row"><h3 class="job-title">New camper trailer retailer requires Logo des...</h3>
        <div class="job-meta"><span><svg viewBox="0 0 10 10"><circle cx="5" cy="5" r="4"/><path d="M5 2.5V5h2"/></svg>3 days left</span><span><svg viewBox="0 0 10 10"><rect x="1" y="2" width="8" height="6"/></svg>58</span><span>$2400</span></div></div>
      <p class="job-desc">We need a fresh take on our retailer request logo. The mark should feel friendly and modern while still working in one color on labels, receipts and signage.</p>
    </article>
    <article class="job featured">
      <div class="watch-tag">Add to<br>watchlist</div>
      <div class="job-row"><h3 class="job-title">Dr. Alma Varga Family Medicine and Aesth...</h3>
        <div class="job-meta"><span><svg viewBox="0 0 10 10"><circle cx="5" cy="5" r="4"/><path d="M5 2.5V5h2"/></svg>3 days left</span><span><svg viewBox="0 0 10 10"><rect x="1" y="2" width="8" height="6"/></svg>58</span><span>$2400</span></div></div>
      <p class="job-desc">Our practice is looking for a refined logo that reflects family care and aesthetic services. Please use calm tones, elegant type and keep the mark simple.</p>
    </article>
    <article class="job">
      <div class="job-row"><h3 class="job-title">Logo Design</h3>
        <div class="job-meta"><span><svg viewBox="0 0 10 10"><circle cx="5" cy="5" r="4"/><path d="M5 2.5V5h2"/></svg>3 days left</span><span><svg viewBox="0 0 10 10"><rect x="1" y="2" width="8" height="6"/></svg>58</span><span>$2400</span></div></div>
      <p class="job-desc">Looking for a memorable logo for a growing studio based in the city. We want something playful, bold and easy to read at small sizes.</p>
    </article>
  </div>

  <div class="section-head"><h2 class="section-title">Achievements (3)</h2><span class="see-all">See all</span></div>
  <div class="card badges">
    <span class="badge"><i></i></span><span class="badge"><i></i></span><span class="badge"><i></i></span><span class="badge"><i></i></span><span class="badge"><i></i></span>
    <span class="badge"><i></i></span><span class="badge"><i></i></span><span class="badge"><i></i></span><span class="badge"><i></i></span><span class="badge"><i></i></span>
  </div>

  <div class="section-head"><h2 class="section-title">Reid M. Castell Reviews</h2><span class="see-all">See all</span></div>
  <div class="card">
    <article class="review">
      <div class="review-head"><h3 class="review-title">Fantastic, quick and friendly service</h3>
        <div class="stars"><svg viewBox="0 0 10 10"><path d="M5 .5 6.4 3.6 9.7 4 7.2 6.2 7.9 9.5 5 7.8 2.1 9.5 2.8 6.2.3 4l3.3-.4z"/></svg><svg viewBox="0 0 10 10"><path d="M5 .5 6.4 3.6 9.7 4 7.2 6.2 7.9 9.5 5 7.8 2.1 9.5 2.8 6.2.3 4l3.3-.4z"/></svg><svg viewBox="0 0 10 10"><path d="M5 .5 6.4 3.6 9.7 4 7.2 6.2 7.9 9.5 5 7.8 2.1 9.5 2.8 6.2.3 4l3.3-.4z"/></svg><svg viewBox="0 0 10 10"><path d="M5 .5 6.4 3.6 9.7 4 7.2 6.2 7.9 9.5 5 7.8 2.1 9.5 2.8 6.2.3 4l3.3-.4z"/></svg><svg viewBox="0 0 10 10"><path d="M5 .5 6.4 3.6 9.7 4 7.2 6.2 7.9 9.5 5 7.8 2.1 9.5 2.8 6.2.3 4l3.3-.4z"/></svg></div>
        <span class="review-date">2 days ago</span></div>
      <p class="review-text">Working with this designer was a pleasure from start to finish. Every request was answered within hours and the revisions were spot on. The final logo looks great on our site and on our cards. Highly recommended for any brand project.</p>
    </article>
    <article class="review">
      <div class="review-head"><h3 class="review-title">New logo for my new business!</h3>
        <div class="stars"><svg viewBox="0 0 10 10"><path d="M5 .5 6.4 3.6 9.7 4 7.2 6.2 7.9 9.5 5 7.8 2.1 9.5 2.8 6.2.3 4l3.3-.4z"/></svg><svg viewBox="0 0 10 10"><path d="M5 .5 6.4 3.6 9.7 4 7.2 6.2 7.9 9.5 5 7.8 2.1 9.5 2.8 6.2.3 4l3.3-.4z"/></svg><svg viewBox="0 0 10 10"><path d="M5 .5 6.4 3.6 9.7 4 7.2 6.2 7.9 9.5 5 7.8 2.1 9.5 2.8 6.2.3 4l3.3-.4z"/></svg><svg viewBox="0 0 10 10"><path d="M5 .5 6.4 3.6 9.7 4 7.2 6.2 7.9 9.5 5 7.8 2.1 9.5 2.8 6.2.3 4l3.3-.4z"/></svg><svg viewBox="0 0 10 10"><path d="M5 .5 6.4 3.6 9.7 4 7.2 6.2 7.9 9.5 5 7.8 2.1 9.5 2.8 6.2.3 4l3.3-.4z"/></svg></div>
        <span class="review-date">2 days ago</span></div>
      <p class="review-text">We asked for a fresh look for our new business and got far more than expected. The concepts were thoughtful, the files were well organized and the whole process was easy. We will be back for our next project soon.</p>
    </article>
    <article class="review">
      <div class="review-head"><h3 class="review-title">Excellent work, fast delivery</h3>
        <div class="stars"><svg viewBox="0 0 10 10"><path d="M5 .5 6.4 3.6 9.7 4 7.2 6.2 7.9 9.5 5 7.8 2.1 9.5 2.8 6.2.3 4l3.3-.4z"/></svg><svg viewBox="0 0 10 10"><path d="M5 .5 6.4 3.6 9.7 4 7.2 6.2 7.9 9.5 5 7.8 2.1 9.5 2.8 6.2.3 4l3.3-.4z"/></svg><svg viewBox="0 0 10 10"><path d="M5 .5 6.4 3.6 9.7 4 7.2 6.2 7.9 9.5 5 7.8 2.1 9.5 2.8 6.2.3 4l3.3-.4z"/></svg><svg viewBox="0 0 10 10"><path d="M5 .5 6.4 3.6 9.7 4 7.2 6.2 7.9 9.5 5 7.8 2.1 9.5 2.8 6.2.3 4l3.3-.4z"/></svg></div>
        <span class="review-date">5 days ago</span></div>
      <p class="review-text">Clear communication, clean work and a great eye for color. Would hire again.</p>
    </article>
  </div>
</main>
</body>
</html>
```